Job Recruiting Agemcy

almost like my current site www.qulvex.com but with these changes see and what i meant about the across the to the site says home job companies categories pages blog and login sign up that should only be the 4 i said only 1 home 2 industries 3 jobs 4 contact us. and remove latest blog post and our partners because that's not us we have to post acuarte information thanks and the name of the company if your using is is work and premier staffing solutions and want it easy for us to post and remove jobs and where it emails us every resume or person that applies

Requirements
Must have
• must send email to us when an application is submitted and try to incorparate the colors of current site
Nice to have
• i want a pretty basic site for now just like the one i have but with all thats above were its easy for me being the own to be able to post jobs and everything

```html
<!DOCTYPE html>
<html lang="en">
<head>
<meta charset="utf-8">
<title>Qulvex – Work and Premier Staffing Solutions</title>
<link href="https://fonts.googleapis.com/css2?family=Rubik:wght@400;500;700&display=swap" rel="stylesheet">
<style>
:root{
  --purple:#6a00e0;
  --purple-deep:#5a00c4;
  --red:#e0434f;
  --ink:#1e1e24;
  --body:#333;
  --lavender:#f6f1fd;
  --card-grey:#f5f3f3;
  --cta:#3a3a3c;
  --footer:#262628;
  --white:#fff;
}
*{box-sizing:border-box;margin:0;padding:0}
html,body{width:1200px;height:3382px;overflow:hidden}
body{position:relative;font-family:'Rubik',Arial,sans-serif;color:var(--body);background:var(--white)}
.abs{position:absolute}
.btn{position:absolute;display:flex;align-items:center;justify-content:center;background:var(--red);color:var(--white);font-weight:500;text-transform:uppercase;letter-spacing:.3px}
.section-title{position:absolute;left:0;width:1200px;text-align:center;font-weight:500;font-size:24px;color:var(--ink);text-transform:uppercase}
.underline{position:absolute;left:583px;width:34px;height:3px;background:var(--purple)}

/* hero */
.hero{left:0;top:0;width:1200px;height:705px;background:linear-gradient(180deg,#54627a 0%,#46536a 45%,#3c475b 100%)}
.brand{position:absolute;display:flex;align-items:center;gap:8px;font-weight:700;color:#c4238a;letter-spacing:1px}
.brand .mark{width:14px;height:14px;background:var(--purple)}
.nav{position:absolute;top:34px;right:26px;display:flex;gap:40px;font-weight:500;font-size:16px;color:var(--white);letter-spacing:.3px}
.hero-title{position:absolute;top:145px;left:0;width:1200px;text-align:center;font-size:32px;font-weight:500;color:var(--white)}
.hero .btn{left:529px;top:211px;width:139px;height:42px;border-radius:21px;font-size:14px;box-shadow:0 4px 10px rgba(0,0,0,.25)}

.search{left:209px;top:658px;width:782px;height:94px;background:var(--purple)}
.search .field{position:absolute;top:26px;height:41px;width:284px;background:var(--white);border-radius:10px;font-size:12px;color:#333;padding-left:17px;display:flex;align-items:center}
.search .btn{left:613px;top:26px;width:146px;height:41px;border-radius:10px;font-size:16px}

/* industries */
.ind-card{position:absolute;top:880px;height:211px;width:222px;border:1px solid #cfcfcf;background:var(--white);text-align:center}
.ind-card svg{position:absolute;left:81px;top:32px}
.ind-card p{position:absolute;left:10px;right:10px;top:123px;font-size:13px;line-height:20px;color:var(--ink)}
.chev{position:absolute;top:970px}

/* welcome */
.welcome{left:0;top:1222px;width:1200px;height:436px;background:var(--lavender)}
.welcome-photo{position:absolute;left:611px;top:0;width:589px;height:436px;background:linear-gradient(120deg,#7d8896 0%,#b9b4ad 45%,#c9c3ba 70%,#8a9199 100%);clip-path:polygon(11px 0,589px 0,589px 436px,39px 436px)}
.welcome-stripe{position:absolute;left:608px;top:0;width:45px;height:436px;background:var(--purple);clip-path:polygon(0 0,5px 0,42px 436px,37px 436px)}
.welcome h2{position:absolute;left:134px;top:46px;font-size:24px;font-weight:500;color:var(--ink)}
.welcome .lead{position:absolute;left:134px;top:110px;width:450px;font-size:16px;line-height:22px;font-weight:500;color:var(--ink)}
.welcome .para{position:absolute;left:134px;top:220px;width:450px;font-size:14px;line-height:20px;color:var(--ink)}

/* jobs */
.jobs{left:0;top:1658px;width:1200px;height:745px;background:linear-gradient(135deg,#7000e6 0%,#6200d8 50%,#6c00e4 100%)}
.job{position:absolute;left:236px;width:757px;height:122px;background:var(--white)}
.job .ico{position:absolute;left:24px;top:30px;width:62px;height:62px;border-radius:50%;background:#f1e9fd;display:flex;align-items:center;justify-content:center}
.job h3{position:absolute;left:101px;top:22px;font-size:14px;font-weight:500;color:var(--ink);text-transform:uppercase}
.job .meta{position:absolute;left:101px;top:45px;font-size:10px;color:#444;display:flex;gap:8px;align-items:center}
.job .desc{position:absolute;left:103px;top:70px;width:450px;font-size:11px;line-height:16px;color:#333}
.job .apply{position:absolute;left:611px;top:40px;width:112px;height:42px;border:2px solid var(--red);color:var(--red);font-weight:500;font-size:14px;display:flex;align-items:center;justify-content:center}

/* testimonials */
.quote{position:absolute;top:2535px;width:298px;height:293px;background:var(--card-grey)}
.quote .qm{position:absolute;left:22px;top:8px;font-size:44px;font-weight:700;color:#b9b6b6;font-family:Georgia,serif}
.quote p{position:absolute;left:43px;top:50px;width:240px;font-size:12.5px;line-height:19px;letter-spacing:-.1px;color:#333}
.quote .rule{position:absolute;left:43px;top:250px;width:34px;height:1px;background:#aaa}
.quote .who{position:absolute;left:43px;top:259px;font-size:10px;font-weight:500;color:var(--ink)}
.round{position:absolute;top:2657px;width:36px;height:36px;border-radius:50%;border:1px solid #bbb;display:flex;align-items:center;justify-content:center}

/* call to action */
.cta{left:0;top:2882px;width:1200px;height:154px;background:var(--cta)}
.cta h2{position:absolute;left:133px;top:45px;font-size:24px;font-weight:500;color:var(--white)}
.cta p{position:absolute;left:133px;top:85px;font-size:17px;color:#eee}
.cta .btn{left:831px;top:49px;width:238px;height:52px;font-size:18px}

/* footer */
.footer{left:0;top:3036px;width:1200px;height:346px;background:var(--footer);color:var(--white)}
.footer h4{position:absolute;top:50px;font-size:13px;font-weight:500;letter-spacing:.3px}
.footer .menu{position:absolute;left:383px;top:86px;font-size:11px;line-height:19.5px;list-style:none}
.f-item{position:absolute;display:flex;align-items:flex-start;gap:12px;font-size:11px;line-height:15px}
.f-item .dot{width:22px;height:22px;border-radius:50%;background:var(--white);display:flex;align-items:center;justify-content:center;flex:none}
.footer .divider{position:absolute;left:133px;top:266px;width:934px;height:1px;background:#3d3d40}
.footer .copy{position:absolute;left:0;top:306px;width:1200px;text-align:center;font-size:9px;color:#ddd}
</style>
</head>
<body>

<!-- Hero -->
<section class="abs hero" role="img" aria-label="Team photo: five smiling professionals holding phones, tablets and laptops against a blue wall">
  <div class="brand" style="left:37px;top:150px;font-size:24px"><span class="mark"></span>QULVEX</div>
  <nav class="nav"><span>HOME</span><span>INDUSTRIES</span><span>JOBS</span><span>CONTACT US</span></nav>
  <h1 class="hero-title">YOUR CAREER STARTS HERE!</h1>
  <a class="btn">Read More</a>
</section>

<form class="abs search">
  <div class="field" style="left:26px">KEYWORDS</div>
  <div class="field" style="left:320px">LOCATION</div>
  <a class="btn">Search</a>
</form>

<!-- Industries -->
<h2 class="section-title" style="top:797px">Industries</h2>
<div class="underline" style="top:838px"></div>

<svg class="chev" style="left:76px" width="18" height="30" viewBox="0 0 18 30"><path d="M15 2 3 15l12 13" fill="none" stroke="#999" stroke-width="2"/></svg>
<svg class="chev" style="left:1099px" width="18" height="30" viewBox="0 0 18 30"><path d="M3 2l12 13L3 28" fill="none" stroke="#999" stroke-width="2"/></svg>

<div class="ind-card" style="left:133px">
  <svg width="60" height="60" viewBox="0 0 60 60" fill="none" stroke="#d9414c" stroke-width="2"><path d="M52 8C38 8 26 18 20 32l8 8c14-6 24-18 24-32z"/><circle cx="38" cy="22" r="5"/><path d="M20 32l-10 2 6-10h10M28 40l-2 10 10-6V34M18 42l-8 8"/></svg>
  <p>Aero Space- Orvan Aero<br>Delk Controls, Stello<br>Brennix Electric</p>
</div>
<div class="ind-card" style="left:370px">
  <svg width="60" height="64" viewBox="0 0 60 64" fill="none" stroke="#d9414c" stroke-width="2"><rect x="4" y="18" width="26" height="40" rx="3"/><rect x="6" y="10" width="22" height="8"/><path d="M17 30v16M9 38h16"/><rect x="32" y="4" width="24" height="54" rx="3"/><circle cx="40" cy="14" r="2.5"/><circle cx="48" cy="14" r="2.5"/><circle cx="40" cy="24" r="2.5"/><circle cx="48" cy="24" r="2.5"/><circle cx="40" cy="34" r="2.5"/><circle cx="48" cy="34" r="2.5"/><circle cx="40" cy="44" r="2.5"/><circle cx="48" cy="44" r="2.5"/></svg>
  <p>Pharmaceutical/<br>Biotechnology Vitacor<br>Lumera cosmetics</p>
</div>
<div class="ind-card" style="left:608px">
  <svg width="60" height="60" viewBox="0 0 80 60" style="left:70px" fill="none" stroke="#d9414c" stroke-width="2.2"><rect x="3" y="12" width="46" height="32" rx="2"/><path d="M49 22h16l10 12v10H49z"/><circle cx="17" cy="48" r="6" fill="#fff"/><circle cx="61" cy="48" r="6" fill="#fff"/></svg>
  <p>Transportation- Hallow<br>Freight, Parcelo</p>
</div>
<div class="ind-card" style="left:846px">
  <svg width="60" height="64" viewBox="0 0 60 64" fill="none" stroke="#d9414c" stroke-width="2"><path d="M30 4v56"/><circle cx="30" cy="8" r="4"/><path d="M30 16C18 8 8 10 2 14c8 2 16 6 28 10 12-4 20-8 28-10-6-4-16-6-28 2z"/><path d="M22 30c10 4 10 10 8 14s-10 6-8 12M38 30c-10 4-10 10-8 14"/></svg>
  <p>Medical - Medrin,<br>Caldora</p>
</div>

<a class="btn" style="left:507px;top:1127px;width:186px;height:35px;font-size:13px">View All Industries</a>

<!-- Welcome -->
<section class="abs welcome">
  <div class="welcome-photo" role="img" aria-label="Photo: recruiter in conversation with a candidate across a desk with laptop"></div>
  <div class="welcome-stripe"></div>
  <h2>WELCOME TO QULVEX</h2>
  <div class="underline" style="left:134px;top:82px"></div>
  <p class="lead">We have over 35 years of Specialized Recruiting and souring experience. We cover a broad spectrum of industries to include some of the top aerospace and pharmaceutical commercial companies of today.</p>
  <p class="para">Lorem ipsum dolor sit amet, consectetur adipiscing elit, sed do eiusmod tempor incididunt ut labore et dolore magna aliqua. Ut enim ad minim veniam, quis nostrud exercitation ullamco laboris nisi ut aliquip ex ea commodo consequat. Duis aute irure dolor in reprehenderit in voluptate velit esse.</p>
  <a class="btn" style="left:138px;top:347px;width:110px;height:35px;font-size:13px">Read More</a>
</section>

<!-- Latest jobs -->
<section class="abs jobs">
  <h2 class="section-title" style="top:49px;color:var(--white)">Latest Jobs</h2>
  <div class="underline" style="top:92px;background:var(--white)"></div>

  <article class="job" style="top:126px">
    <div class="ico"><svg width="34" height="34" viewBox="0 0 34 34" fill="none" stroke="#6a00e0" stroke-width="1.6"><rect x="3" y="4" width="28" height="22" rx="2"/><path d="M3 9h28M9 15h6M9 19h4"/><circle cx="22" cy="21" r="5"/><circle cx="22" cy="21" r="2"/></svg></div>
    <h3>Software Engineering</h3>
    <div class="meta"><span>⌖ England</span><span>|</span><span>◷ Full Time</span></div>
    <p class="desc">Lorem ipsum dolor sit amet, consectetur adipiscing elit, sed do eiusmod tempor incididunt ut labore et dolore magna aliqua.</p>
    <a class="apply">APPLY JOB</a>
  </article>
  <article class="job" style="top:259px">
    <div class="ico"><svg width="34" height="34" viewBox="0 0 34 34" fill="none" stroke="#6a00e0" stroke-width="1.6"><circle cx="17" cy="17" r="6"/><path d="M17 3v5M17 26v5M3 17h5M26 17h5M7 7l3.5 3.5M23.5 23.5 27 27M7 27l3.5-3.5M23.5 10.5 27 7"/><circle cx="17" cy="17" r="11"/></svg></div>
    <h3>Architecture and Engineering Occupations</h3>
    <div class="meta"><span>⌖ England</span><span>|</span><span>◷ Full Time</span></div>
    <p class="desc">Lorem ipsum dolor sit amet, consectetur adipiscing elit, sed do eiusmod tempor incididunt ut labore et dolore magna aliqua.</p>
    <a class="apply">APPLY JOB</a>
  </article>
  <article class="job" style="top:392px">
    <div class="ico"><svg width="34" height="34" viewBox="0 0 34 34" fill="none" stroke="#6a00e0" stroke-width="1.6"><rect x="3" y="10" width="28" height="18" rx="2"/><path d="M12 10V6h10v4M3 17h28M15 17v3h4v-3"/></svg></div>
    <h3>Business and Financial Operations</h3>
    <div class="meta"><span>⌖ England</span><span>|</span><span>◷ Full Time</span></div>
    <p class="desc">Lorem ipsum dolor sit amet, consectetur adipiscing elit, sed do eiusmod tempor incididunt ut labore et dolore magna aliqua.</p>
    <a class="apply">APPLY JOB</a>
  </article>
  <article class="job" style="top:523px">
    <div class="ico"><svg width="34" height="34" viewBox="0 0 34 34" fill="none" stroke="#6a00e0" stroke-width="1.6"><rect x="3" y="6" width="28" height="18" rx="2"/><path d="M7 10h20v10H7zM13 24v4h8v-4M10 28h14"/></svg></div>
    <h3>Computer and Mathematical</h3>
    <div class="meta"><span>⌖ England</span><span>|</span><span>◷ Full Time</span></div>
    <p class="desc">Lorem ipsum dolor sit amet, consectetur adipiscing elit, sed do eiusmod tempor incididunt ut labore et dolore magna aliqua.</p>
    <a class="apply">APPLY JOB</a>
  </article>

  <a class="btn" style="left:530px;top:671px;width:140px;height:36px;font-size:13px">View All Jobs</a>
</section>

<!-- Testimonials -->
<h2 class="section-title" style="top:2448px">Testimonials</h2>
<div class="underline" style="top:2489px"></div>

<div class="round" style="left:58px"><svg width="10" height="16" viewBox="0 0 10 16"><path d="M8 2 2 8l6 6" fill="none" stroke="#999" stroke-width="1.5"/></svg></div>
<div class="round" style="left:1101px"><svg width="10" height="16" viewBox="0 0 10 16"><path d="M2 2l6 6-6 6" fill="none" stroke="#999" stroke-width="1.5"/></svg></div>

<article class="quote" style="left:131px">
  <span class="qm">“</span>
  <p>"I was highly impressed by the professionalism shown during my interview process. It was less an interview and more of a conversation with the recruiter. I felt comfortable sharing my previous management experience and all of my qualifications for the Operations Manager position. I was informed about Harbor Smile® History, Mission and Values</p>
  <span class="rule"></span><span class="who">Marla Tenney</span>
</article>
<article class="quote" style="left:452px">
  <span class="qm">“</span>
  <p>Lorem ipsum dolor sit amet, cons ectetur adipiscing elit, sed do eius mod tempor incididunt ut labore et dolore magna aliqua. Ut enim ad minim veniam, quis nostrud exer citation ullamco laboris nisi ut aliq uip ex ea commodo consequat. Duis aute irure dolor in reprehe nderit in voluptate velit esse.</p>
  <span class="rule"></span><span class="who">DORIAN</span>
</article>
<article class="quote" style="left:771px">
  <span class="qm">“</span>
  <p>Lorem ipsum dolor sit amet, cons ectetur adipiscing elit, sed do eius mod tempor incididunt ut labore et dolore magna aliqua. Ut enim ad minim veniam, quis nostrud exer citation ullamco laboris nisi ut aliq uip ex ea commodo consequat. Duis aute irure dolor in reprehe nderit in voluptate velit esse.</p>
  <span class="rule"></span><span class="who">DORIAN</span>
</article>

<!-- Call to action -->
<section class="abs cta">
  <h2>SEEKING FOR A JOB?</h2>
  <p>Browse hundreds of job offers and find the best suitable position.</p>
  <a class="btn">Apply Job</a>
</section>

<!-- Footer -->
<footer class="abs footer">
  <div class="brand" style="left:135px;top:150px;font-size:22px"><span class="mark"></span>QULVEX</div>

  <h4 style="left:383px">MENU</h4>
  <ul class="menu"><li>HOME</li><li>INDUSTRIES</li><li>JOBS</li><li>CONTACT US</li></ul>

  <h4 style="left:626px">CONTACT US</h4>
  <div class="f-item" style="left:626px;top:90px"><span class="dot"><svg width="10" height="12" viewBox="0 0 10 12"><path d="M5 11S1 6.5 1 4a4 4 0 0 1 8 0c0 2.5-4 7-4 7z" fill="#262628"/><circle cx="5" cy="4" r="1.4" fill="#fff"/></svg></span><span>18 Linden Row, Suite 204<br>Fairhaven, OR 97410, USA</span></div>
  <div class="f-item" style="left:626px;top:141px"><span class="dot"><svg width="11" height="11" viewBox="0 0 12 12"><path d="M2 1h3l1 3-1.5 1a6 6 0 0 0 2.5 2.5L8 6l3 1v3c0 .6-.4 1-1 1C5 11 1 7 1 2c0-.6.4-1 1-1z" fill="#262628"/></svg></span><span>Call Us<br>+1 555 010 482</span></div>
  <div class="f-item" style="left:626px;top:192px"><span class="dot"><svg width="11" height="9" viewBox="0 0 12 9"><rect x="0.5" y="0.5" width="11" height="8" fill="#262628"/><path d="M1 1l5 4 5-4" fill="none" stroke="#fff"/></svg></span><span>E mail Us<br>hello@qulvex.com</span></div>

  <h4 style="left:962px">FOLLOW US</h4>
  <div class="f-item" style="left:962px;top:90px"><span class="dot"></span><span>Like us on<br>FEEDLINE</span></div>
  <div class="f-item" style="left:962px;top:140px"><span class="dot"></span><span>Follow us on<br>CHIRPER</span></div>
  <div class="f-item" style="left:962px;top:190px"><span class="dot"></span><span>Follow us on<br>WORKNET</span></div>

  <div class="divider"></div>
  <p class="copy">Copyright © 2020 All Rights Reserved</p>
</footer>

</body>
</html>
```